Mr. Kelpie Restaurant Menu Design

I would like for you to please create a menu design for my seafood restaurant called Mr. Kelpie. I uploaded the logo of my restaurant and would like the same colors and font to be used on the menu. The headings of my menu should include the following:
What's your catch?
What's your sauce?
How "Hot" can you go?
Medium?
Mild?
Wild?
Soups
Paella
Katsu
Add Ons
Sweet Cravings
Thirsty?
It would be nice to see something creative and simple preferably one page.
I already uploaded my logo on the brief section.
Thank you.
Target Market(s)
Family friendly
Industry/Entity Type
Seafood Restaurant
Look and feel

```html
<!DOCTYPE html>
<html lang="en">
<head>
<meta charset="utf-8">
<title>Mr. Kelpie Restaurant Menu</title>
<link href="https://fonts.googleapis.com/css2?family=Lilita+One&family=Arimo:wght@400;700&display=swap" rel="stylesheet">
<style>
  :root {
    --sea: #2a9fd8;
    --sea-light: #5cc0ea;
    --sea-deep: #1b7fba;
    --orange: #f7821f;
    --orange-shadow: #8a3d0c;
    --ink: #111111;
    --card: #ffffff;
  }
  * { box-sizing: border-box; margin: 0; padding: 0; }
  html, body { width: 848px; height: 1200px; overflow: hidden; }
  body { font-family: "Arimo", Arial, sans-serif; color: var(--ink); }
  .menu { position: relative; width: 848px; height: 1200px; overflow: hidden; }
  .sea-pattern {
    position: absolute; inset: 0;
    background: linear-gradient(160deg, var(--sea-light) 0%, var(--sea) 45%, var(--sea-deep) 100%);
  }
  .card {
    position: absolute; background: var(--card);
    box-shadow: 0 4px 10px rgba(0,0,0,.35);
    padding: 14px 24px;
  }
  .card--right { border-radius: 0 28px 28px 0; }
  .card--left { border-radius: 28px 0 0 28px; }
  .section-title {
    font-family: "Lilita One", "Arial Black", sans-serif;
    color: var(--orange); font-size: 44px; line-height: 1; text-align: center;
    text-shadow: 2px 3px 0 var(--orange-shadow);
    letter-spacing: .5px;
  }
  .item { font-size: 16px; line-height: 1.22; margin-bottom: 12px; }
  .item h3 { font-size: 16px; font-weight: 700; }
  .cols { display: grid; gap: 0 20px; margin-top: 10px; }
  .cols--2 { grid-template-columns: 1fr 1fr; }
  .cols--3 { grid-template-columns: 1fr 1fr 1fr; }

  .brand {
    position: absolute; left: 70px; top: 80px; width: 220px;
    display: flex; align-items: center; gap: 10px;
  }
  .brand__dot { width: 18px; height: 18px; border-radius: 50%; background: var(--card); flex: none; }
  .brand__name { font-family: "Arimo", Arial, sans-serif; font-weight: 700; font-size: 26px; color: var(--card); }

  .catch { left: 356px; top: 28px; width: 492px; height: 454px; padding-top: 12px; }
  .catch .section-title { font-size: 46px; }
  .catch .cols { gap: 0 14px; margin-top: 8px; }
  .catch .item { margin-bottom: 10px; }
  .soups { left: 0; top: 214px; width: 336px; height: 268px; }

  .sauce { left: 0; top: 502px; width: 445px; height: 143px; padding-top: 10px; text-align: center; }
  .sauce .section-title { font-size: 31px; }
  .sauce__prices { display: flex; justify-content: center; gap: 30px; font-size: 16px; margin: 6px 0 8px; }
  .heat { display: flex; justify-content: center; gap: 14px; margin-top: 6px; }
  .heat span { font-family: "Lilita One", sans-serif; color: var(--orange); font-size: 15px; text-shadow: 1px 1px 0 var(--orange-shadow); }

  .paella { left: 470px; top: 502px; width: 378px; height: 143px; }
  .addons { left: 0; top: 658px; width: 445px; height: 171px; }
  .katsu { left: 470px; top: 658px; width: 378px; height: 171px; }

  .thirsty { left: 0; top: 849px; width: 311px; height: 322px; padding: 14px 30px 14px 44px; }
  .drinks { margin-top: 12px; font-size: 16px; line-height: 1.24; }
  .drinks h3 { font-size: 16px; font-weight: 700; }
  .drinks ul { list-style: none; margin-bottom: 12px; }
  .drinks li { display: grid; grid-template-columns: 1fr 70px; gap: 16px; }
  .drinks li span:first-child { text-align: right; }

  .sweets { left: 331px; top: 849px; width: 517px; height: 322px; }
  .sweets .cols { gap: 0 18px; }
</style>
</head>
<body>
<main class="menu">
  <div class="sea-pattern" role="img" aria-label="Blue sea background with white wave pattern"></div>

  <div class="brand">
    <span class="brand__dot"></span>
    <span class="brand__name">Mr. Kelpie</span>
  </div>

  <section class="card card--left catch">
    <h2 class="section-title">What's your catch?</h2>
    <div class="cols cols--2">
      <div>
        <div class="item"><h3>Lorem ipsum</h3>Dolor sit amet, consectetur adipiscing elit. Integer nec. Craesent libero. $9.99</div>
        <div class="item"><h3>Lorem ipsum</h3>Dolor sit amet, consectetur adipiscing elit. Integer nec odio. Sed cursus ante dapibus diam. $9.99</div>
        <div class="item"><h3>Lorem ipsum</h3>Dolor sit amet, consectetur adipiscing elit. Integer nec odio. Praesent lbero. $9.99</div>
        <div class="item"><h3>Lorem ipsum</h3>Dolor sit amet. Sed cursus ante dapibus diam. Integer nec odio. $9.99</div>
      </div>
      <div>
        <div class="item"><h3>Lorem ipsum</h3>Dolor sit amet, consectetur adipiscing elit. Integer nec odio. Praesent. $9.99</div>
        <div class="item"><h3>Lorem ipsum</h3>Dolor sit amet, consectetur adipiscing elit. Integer nec odio. Praesent libero. $9.99</div>
        <div class="item"><h3>Lorem ipsum</h3>Dolor sit amet, consectetur adipiscing elit. Integer nec odio. $9.99</div>
        <div class="item"><h3>Lorem ipsum</h3>Dolor sit amet, consectetur adipiscing elit. Integer nec odio. Praesent libero.Integer nec odio. $9.99</div>
      </div>
    </div>
  </section>

  <section class="card card--right soups">
    <h2 class="section-title">Soups</h2>
    <div class="cols cols--2">
      <div>
        <div class="item"><h3>Lorem ipsum</h3>Dolor sit amet, consectur. Integer nec. $9.99</div>
        <div class="item"><h3>Lorem ipsum</h3>dolor sit amet, consectetur necace. $9.99</div>
      </div>
      <div>
        <div class="item"><h3>Lorem ipsum</h3>Dolor sit amet, cotetur, consectetur adipiscing elit. Integer nec odio. Praesent lbero. Dolor sit to ametet. $9.99</div>
      </div>
    </div>
  </section>

  <section class="card card--right sauce">
    <h2 class="section-title">What's your sauce?</h2>
    <div class="sauce__prices"><span>Praesent libero. $9.99</span><span>Praesent libero. $9.99</span></div>
    <h2 class="section-title">How "Hot" can you go?</h2>
    <div class="heat"><span>Medium?</span><span>Mild?</span><span>Wild?</span></div>
  </section>

  <section class="card card--left paella">
    <h2 class="section-title">Paella</h2>
    <div class="cols cols--2">
      <div class="item"><h3>Lorem ipsum</h3>dolor sit amet nec integer. $9.99</div>
      <div class="item"><h3>Lorem ipsum</h3>dolor sit amet, consectetur. $9.99</div>
    </div>
  </section>

  <section class="card card--right addons">
    <h2 class="section-title">Add Ons</h2>
    <div class="cols cols--3">
      <div class="item"><h3>Lorem ipsum</h3>Dolor sit amet, consectetur odiole ne. $9.99</div>
      <div class="item"><h3>Lorem ipsum</h3>Dolor sit amet, consectetur necace. $9.99</div>
      <div class="item"><h3>Lorem ipsum</h3>Dolor sit amet, consectetur integer. $9.99</div>
    </div>
  </section>

  <section class="card card--left katsu">
    <h2 class="section-title">Katsu</h2>
    <div class="cols cols--2">
      <div class="item"><h3>Lorem ipsum</h3>Dolor sit amet, adipiscing elit. Integer nec . $9.99</div>
      <div class="item"><h3>Lorem ipsum</h3>Dolor sit amet, Iger nec odio. Praesent libero tu. $9.99</div>
    </div>
  </section>

  <section class="card card--right thirsty">
    <h2 class="section-title">Thirsty?</h2>
    <div class="drinks">
      <h3>Lorem ipsum amet</h3>
      <ul>
        <li><span>Dolor sit</span><span>$2.99</span></li>
        <li><span>Consectetur</span><span>$2.99</span></li>
        <li><span>Odilole</span><span>$2.99</span></li>
        <li><span>Amet sit</span><span>$2.99</span></li>
        <li><span>Integer dolar</span><span>$2.99</span></li>
      </ul>
      <h3>Lorem ipsum Odiloe</h3>
      <ul>
        <li><span>Dolor sit</span><span>$2.99</span></li>
        <li><span>Consectetur</span><span>$2.99</span></li>
        <li><span>Odilole</span><span>$2.99</span></li>
        <li><span>Amet sit</span><span>$2.99</span></li>
      </ul>
    </div>
  </section>

  <section class="card card--left sweets">
    <h2 class="section-title">Sweet Cravings</h2>
    <div class="cols cols--2">
      <div>
        <div class="item"><h3>Lorem ipsum</h3>Dolor sit amet, consectetur adipiscing elit. Integer nec odio. Sed cursus ante dapibus diam. $9.99</div>
        <div class="item"><h3>Lorem ipsum</h3>Dolor sit amet, consectetur adipiscing elit. Integer nec odio. Praesent lbero. $9.99</div>
        <div class="item"><h3>Lorem ipsum</h3>Dolor sit amet. $9.99</div>
      </div>
      <div>
        <div class="item"><h3>Lorem ipsum</h3>Dolor sit amet, consectetur adipiscing elit. Integer nec odio. Praesent libero. $9.99</div>
        <div class="item"><h3>Lorem ipsum</h3>Dolor sit amet, consectetur adipiscing elit. Integer nec odio. $9.99</div>
        <div class="item"><h3>Lorem ipsum</h3>Dolor sit amet. Sed cursus ante dapibus diam. $9.99</div>
      </div>
    </div>
  </section>
</main>
</body>
</html>
```